Law Firm Needs Brochure Redesign Using New Logo

We are a personal injury law firm that does auto injuries and other personal injury cases. We want a new brochure that has our updated logo and information. Instead of gold and black, we want more navy, as matches the new logo. The Auto Liability portion should read: "(required by the state of Arizona in the amounts of $25,000 per person / $50,000 per accident, but a higher amount may be best )." The other information can remain the same. We'd like the brochure to keep the same professional tone as the previous brochure.
Our website is https://www.marbrenlegal.com/.

```html
<!DOCTYPE html>
<html lang="en">
<head>
<meta charset="utf-8">
<title>Marbren Legal – Car Accident Brochure</title>
<link rel="stylesheet" href="https://fonts.googleapis.com/css2?family=Arimo:wght@400;700&display=swap">
<style>
  :root {
    --navy: #13294b;
    --white: #ffffff;
    --mist-top: #b3bac5;
    --mist-mid: #6f7886;
    --forest: #2a3340;
    --road: #8d949e;
    --road-low: #a4aab2;
    --car-dark: #2b1f19;
    --car-warm: #6b4a37;
    --car-sky: #c9c3bb;
    --car-body: #8c9096;
  }
  * { margin: 0; padding: 0; box-sizing: border-box; }
  html, body { width: 1200px; height: 931px; overflow: hidden; background: var(--white); }
  body { font-family: "Arimo", Arial, sans-serif; }
  .brochure { position: relative; width: 1200px; height: 931px; }

  .panel { position: absolute; top: 0; height: 931px; overflow: hidden; }
  .panel--stats { left: 0; width: 401px; }
  .panel--mailer { left: 401px; width: 397px; background: var(--white); }
  .panel--cover { left: 798px; width: 402px; }

  .photo { position: absolute; inset: 0; }
  .photo--valley {
    background: linear-gradient(180deg, var(--mist-top) 0%, #9aa2ae 28%, var(--mist-mid) 42%, var(--forest) 60%, #252e3a 66%, var(--road) 66.5%, var(--road-low) 100%);
  }
  .photo--car {
    background:
      radial-gradient(ellipse 70% 55% at 80% 72%, var(--car-body) 0%, #5d6168 45%, transparent 75%),
      linear-gradient(200deg, var(--car-sky) 0%, var(--car-warm) 30%, var(--car-dark) 65%, #3a2a20 100%);
  }

  .stat { position: absolute; left: 0; width: 401px; text-align: center; color: var(--white); }
  .stat__over { font-size: 25px; line-height: 1; }
  .stat__figure { font-weight: 700; line-height: 1; letter-spacing: -1px; }
  .stat__caption { font-size: 16px; line-height: 20px; }
  .stat--crashes { top: 158px; }
  .stat--crashes .stat__figure { font-size: 74px; margin-top: 12px; }
  .stat--crashes .stat__caption { margin-top: 14px; }
  .stat--fatal { top: 390px; }
  .stat--fatal .stat__figure { font-size: 74px; margin-top: 14px; }
  .stat--fatal .stat__caption { margin-top: 2px; }

  .rule { position: absolute; left: 55px; width: 311px; height: 8px; }
  .rule--light { top: 595px; background: var(--white); }
  .rule--navy { top: 637px; background: var(--navy); }

  .wordmark { font-weight: 700; color: var(--navy); letter-spacing: 1px; white-space: nowrap; }
  .panel--stats .wordmark { position: absolute; top: 683px; left: 0; width: 401px; text-align: center; font-size: 32px; }

  .promise {
    position: absolute; top: 763px; left: 30px; width: 341px;
    text-align: center; color: var(--navy); font-size: 15px; line-height: 18.7px;
  }

  .mailer-block {
    position: absolute; left: 440px; top: 896px;
    transform: rotate(-90deg); transform-origin: left top;
    display: flex; align-items: flex-start; gap: 30px;
  }
  .panel--mailer .wordmark { font-size: 30px; line-height: 34px; margin-top: 2px; }
  .address { color: var(--navy); font-size: 16px; line-height: 20px; margin-left: 24px; margin-top: 96px; }
  .mailer-wrap { position: absolute; left: 0; top: 0; }

  .cover-head { position: absolute; left: 34px; top: 40px; color: var(--white); font-size: 26px; line-height: 31px; }
  .cover-sub { position: absolute; left: 36px; top: 162px; color: var(--white); font-size: 20px; line-height: 26px; }
  .panel--cover .wordmark { position: absolute; right: 86px; bottom: 32px; color: var(--white); font-size: 26px; }
</style>
</head>
<body>
<main class="brochure">

  <section class="panel panel--stats">
    <div class="photo photo--valley" role="img" aria-label="Photo of a mountain road running through a pine forest valley under cloudy sky, toned blue-grey"></div>
    <div class="stat stat--crashes">
      <p class="stat__over">OVER</p>
      <p class="stat__figure">107,000</p>
      <p class="stat__caption">crashes will happen in the state of<br>Arizona this year.</p>
    </div>
    <div class="stat stat--fatal">
      <p class="stat__over">OVER</p>
      <p class="stat__figure">700</p>
      <p class="stat__caption">of them will result in fatalities.</p>
    </div>
    <div class="rule rule--light"></div>
    <div class="rule rule--navy"></div>
    <p class="wordmark">MARBREN LEGAL</p>
    <p class="promise">If we don’t win, you don’t pay<br>attorney fees. That seems fair to us.<br>Know what’s happening with your<br>case, get the answers to your<br>questions and work on getting better<br>with confidence that you’ve got<br>an excellent group of people working for you.</p>
  </section>

  <section class="panel panel--mailer"></section>
  <div class="mailer-block">
    <p class="wordmark">MARBREN LEGAL</p>
    <p class="address">4870 W. Canyon Road Suite B110<br>Phoenix AZ 85031</p>
  </div>

  <section class="panel panel--cover">
    <div class="photo photo--car" role="img" aria-label="Photo of a silver sedan's front and headlights parked beneath a bridge in warm light"></div>
    <h1 class="cover-head">Protect your family<br>in case of a<br>car accident</h1>
    <p class="cover-sub">A little knowledge<br>and preparation<br>go along way</p>
    <p class="wordmark">MARBREN LEGAL</p>
  </section>

</main>
</body>
</html>
```